Diabetes Education Flyer Design Project

We need a 8.5" X 11" flyer design for a retail pharmacy located in Queens, NYC to promote our new program of "Free Diabetes Education". This flyer will be distributed to doctors offices and to places where people congregate. The flyer should create a fear to the audience about diabetes and an urgency to come or call the pharmacy to get more information on the "Free Diabetes Education". The target audience is 40+ years old with national background of West Indies and India. They are mostly blue color worker with a highschool or less education

Target Market(s)

People with diabetes aging 40+, from West Indies and India, low literacy level

Industry/Entity Type

Education

Requirements
Must have
• Must have graphics and colors to attract the targetted age/race/literacy. Must have graphics and colors to create fear at the begining and hope at the end.
Nice to have
• Fonts to support the theme

```html
<!DOCTYPE html>
<html lang="en">
<head>
<meta charset="utf-8">
<title>Free Diabetes Education Flyer</title>
<link href="https://fonts.googleapis.com/css2?family=Roboto+Condensed:wght@300;400;700&display=swap" rel="stylesheet">
<style>
  :root {
    --red: #c8102e;
    --red-dark: #8e0b1f;
    --blue: #1f3f9a;
    --ink: #1a1a1a;
    --grey-bg: #f1f1f1;
    --black: #000000;
    --white: #ffffff;
  }
  * { margin: 0; padding: 0; box-sizing: border-box; }
  html, body { width: 927px; height: 1200px; overflow: hidden; background: var(--white); }
  .flyer {
    position: relative;
    width: 927px;
    height: 1200px;
    overflow: hidden;
    font-family: "Roboto Condensed", "Arial Narrow", sans-serif;
    color: var(--ink);
    background: linear-gradient(180deg, #ffffff 55%, var(--grey-bg) 85%);
  }
  .hero-photo {
    position: absolute;
    left: 0; top: 0;
    width: 927px; height: 640px;
    background:
      radial-gradient(ellipse 340px 300px at 640px 260px, #5a3a2a 0%, #7a5a48 30%, rgba(230,228,222,0) 70%),
      radial-gradient(ellipse 420px 220px at 600px 470px, #f3f1ec 0%, rgba(240,238,232,0) 75%),
      linear-gradient(90deg, #d9dcdc 0%, #eef0ef 40%, #e6e8e6 70%, #cfd3d3 100%);
  }
  .hero-wave { position: absolute; left: 0; top: 420px; width: 927px; height: 230px; }
  .brand-top {
    position: absolute;
    left: 58px; top: 48px;
    display: flex; align-items: center; gap: 10px;
    font-weight: 700; font-size: 40px; letter-spacing: 0.5px;
    color: var(--blue);
    text-transform: uppercase;
  }
  .brand-mark { width: 22px; height: 22px; background: var(--red); border-radius: 50%; }
  .headline {
    position: absolute; left: 52px; top: 618px;
    font-weight: 700; font-size: 112px; line-height: 1;
    color: var(--red); letter-spacing: 1px;
    text-transform: uppercase;
  }
  .claim {
    position: absolute; left: 54px; top: 748px;
    font-weight: 400; font-size: 48px; line-height: 56px;
    color: var(--ink);
  }
  .claim .figure { color: var(--red); }
  .claim sup { font-size: 20px; vertical-align: 22px; margin-left: 6px; }
  .offer {
    position: absolute; right: 496px; top: 928px;
    text-align: right;
    font-size: 21px; line-height: 31px; font-weight: 400;
  }
  .brand-small {
    display: inline-flex; align-items: center; gap: 6px;
    font-weight: 700; font-size: 24px; color: var(--blue);
    text-transform: uppercase; margin-bottom: 12px;
  }
  .brand-small .brand-mark { width: 13px; height: 13px; }
  .offer strong { font-weight: 700; }
  .contact-box {
    position: absolute; left: 465px; top: 920px;
    width: 462px; height: 159px;
    background: linear-gradient(180deg, var(--red) 0%, var(--red-dark) 100%);
    color: var(--white);
    padding: 22px 24px;
  }
  .contact-cta { font-weight: 700; font-size: 30px; line-height: 34px; }
  .contact-address { font-weight: 400; font-size: 21px; line-height: 30px; margin-top: 8px; }
  .contact-phone { font-weight: 700; font-size: 36px; line-height: 44px; margin-top: 6px; }
  .footnote-bar {
    position: absolute; left: 0; top: 1133px;
    width: 927px; height: 67px;
    background: var(--black); color: var(--white);
    font-size: 10.5px; font-weight: 300;
    padding: 26px 36px 0;
  }
</style>
</head>
<body>
<main class="flyer">
  <div class="hero-photo" role="img" aria-label="Photo of a worried middle-aged man in a white shirt leaning back in a green chair"></div>

  <svg class="hero-wave" viewBox="0 0 927 230" preserveAspectRatio="none" aria-hidden="true">
    <defs>
      <linearGradient id="waveRed" x1="0" y1="0" x2="1" y2="0">
        <stop offset="0" stop-color="#8e0b1f"/>
        <stop offset="0.5" stop-color="#c8102e"/>
        <stop offset="1" stop-color="#8e0b1f"/>
      </linearGradient>
    </defs>
    <path d="M0 40 C 220 10, 420 20, 620 90 S 860 170, 927 150 L 927 230 L 0 230 Z" fill="url(#waveRed)"/>
    <path d="M0 62 C 220 36, 420 48, 620 118 S 860 196, 927 178 L 927 230 L 0 230 Z" fill="#ffffff"/>
  </svg>

  <div class="brand-top"><span>Harbor Pharmacy</span><span class="brand-mark"></span></div>

  <h1 class="headline">Diabetes</h1>
  <p class="claim">Kills <span class="figure">3,400,000</span> People In a Year<sup>1</sup><br>Are You the Next?</p>

  <div class="offer">
    <div class="brand-small"><span>Harbor Pharmacy</span><span class="brand-mark"></span></div>
    <p>Is Offering <strong>FREE</strong> Education for Diabetics.</p>
    <p>Your Life Depends on It!</p>
    <p>Educate Yourself and Live Longer.</p>
  </div>

  <section class="contact-box">
    <p class="contact-cta">Call or Stop by Now!</p>
    <p class="contact-address">204-38 Maple Ave., Oak Ridge, NY 11420</p>
    <p class="contact-phone">(555) 014-2870</p>
  </section>

  <footer class="footnote-bar">
    <sup>1</sup>According to International Health Bureau in 2004, an estimated 3.4 million people died worldwide from consequences of high blood sugar. Fact Sheet No. 312 (August, 2011)
  </footer>
</main>
</body>
</html>
```